Stationery Design Project

Would like to have the design elements we created in for our website (www.brook-holdings.example), incorporated in a stationery design layout.
Updates
Colors used in the logo attachments do not need to be used. We are open to different color variations. Looking for a crisp, clean, modern update using the design elements in attachments and which can also be viewed on or website.
A note to designers:
Project Deadline Extended
Reason: Due to update in our project description and requirements, we have decided to extend the deadline of this project to provide ample opportunity to all designers participating .
Requirements
Must have
- Must have continuity with the theme and design features used in our website. Have attached .jpg images of some of the design elements.

```html
<!DOCTYPE html>
<html lang="en">
<head>
<meta charset="utf-8">
<title>Brook Holdings Inc — Letterhead</title>
<link rel="stylesheet" href="https://fonts.googleapis.com/css2?family=Source+Sans+3:wght@400;600&family=Arimo:wght@400&display=swap">
<style>
  :root {
    --brand-green: #58ae43;
    --brand-blue: #0a8ccf;
    --name-blue: #1b7cbf;
    --frame-grey: #b9bcbe;
    --footer-grey: #6b6e70;
    --mark-grey: #eeeeef;
    --paper: #ffffff;
  }
  * { margin: 0; padding: 0; box-sizing: border-box; }
  html, body {
    width: 900px; height: 1200px; overflow: hidden;
    background: var(--paper);
  }
  .letterhead {
    position: relative;
    width: 900px; height: 1200px;
    background: var(--paper);
  }
  .sheet-frame {
    position: absolute;
    left: 19px; top: 25px; width: 863px; height: 1150px;
    border: 1px solid var(--frame-grey);
  }
  .accent-bar {
    position: absolute; left: 19px; width: 863px; display: flex;
  }
  .accent-bar--top { top: 25px; height: 20px; }
  .accent-bar--bottom { top: 1166px; height: 8px; }
  .accent-bar .green { background: var(--brand-green); }
  .accent-bar .blue { background: var(--brand-blue); flex: 1; }
  .accent-bar--top .green { width: 494px; }
  .accent-bar--bottom .green { width: 533px; }
  .header-glow {
    position: absolute; left: 20px; top: 127px; width: 861px; height: 18px;
    display: flex;
  }
  .header-glow .green {
    width: 493px;
    background: linear-gradient(to bottom, #dcefe3 0%, #f2f9f4 45%, rgba(255,255,255,0) 100%);
  }
  .header-glow .blue {
    flex: 1;
    background: linear-gradient(to bottom, #d9ecf6 0%, #f1f8fc 45%, rgba(255,255,255,0) 100%);
  }
  .header-rule {
    position: absolute; left: 20px; top: 127px; width: 861px; height: 1px;
    background: #e3ecee;
  }
  .company-name {
    position: absolute; left: 64px; top: 70px;
    font-family: "Source Sans 3", "Myriad Pro", sans-serif;
    font-weight: 400; font-size: 44px; line-height: 1;
    letter-spacing: -0.5px;
    color: var(--name-blue);
  }
  .website {
    position: absolute; left: 627px; top: 81px;
    font-family: Arimo, Arial, sans-serif;
    font-size: 13px; color: var(--brand-green);
  }
  .watermark-name {
    position: absolute; left: 118px; top: 1010px;
    font-family: "Source Sans 3", "Myriad Pro", sans-serif;
    font-weight: 400; font-size: 98px; line-height: 1;
    letter-spacing: -1px;
    color: var(--mark-grey);
    white-space: nowrap;
  }
  .footer-contact {
    position: absolute; left: 0; width: 900px; top: 1131px;
    text-align: center;
    font-family: Arimo, Arial, sans-serif;
    font-size: 12.5px; color: var(--footer-grey);
  }
</style>
</head>
<body>
  <main class="letterhead">
    <div class="sheet-frame"></div>

    <div class="accent-bar accent-bar--top"><span class="green"></span><span class="blue"></span></div>
    <div class="header-glow"><span class="green"></span><span class="blue"></span></div>
    <div class="header-rule"></div>

    <h1 class="company-name">Brook Holdings Inc</h1>
    <p class="website">www.brook-holdings.example</p>

    <div class="watermark-name" aria-hidden="true">Brook Holdings Inc</div>

    <p class="footer-contact">418-Mill Creek Lane Suite 120, Riverton, GA - 30999,&nbsp; Phone : (555) 014-2236, Fax : (555) 014-2290,info@brook-holdings.example</p>

    <div class="accent-bar accent-bar--bottom"><span class="green"></span><span class="blue"></span></div>
  </main>
</body>
</html>
```